Stationery Design Project for Lotvian, Chicago

Lotvian, a street parking application which helps car drivers find a street parking spot by offering an ideal path along which to look for parking. This path is calculated by our algorithm based on data (e.g. historical data, baseball games schedule, etc.). Along this path the driver will find a spot and will also save 70% of the search time. Customer we target is reg. between 21 and 45 yo.

We envision something young, fresh, bright and original. Slightly abstract maybe. It should represent the idea and elements of finding street parking in the city, e.g. car(s), parking spot, people, city, etc. (just ideas!).

Requirement:
- Business Cards (2 Sided Full Color CMYK)
- Letterhead (1 Sided Full Color CMYK)
- Envelope (1 Sided Full Color CMYK)
- Sticker (1 Sided Full Color CMYK), round with a 2inch diameter.

Reason: We're starting to get more and more designs and need more time to look into all of them. Very exciting!! Thanks to everybody!

Hi all, we're in the process of selecting our favs. Though choices!!! Really good submissions. Will keep you posted and sorry for the delay.

Target Market(s)

Car drivers and owners between 21 and 45

Industry/Entity Type

Parking

Requirements
Must have
• Sticker should be round and include company URL lotvian.com and the new logo which we will attach soon.
Should not have
• Should not be too serious or boring.

```html
<!DOCTYPE html>
<html lang="en">
<head>
<meta charset="utf-8">
<title>Lotvian – Business Card, Front and Back</title>
<link rel="stylesheet" href="https://fonts.googleapis.com/css2?family=Source+Sans+3:wght@400;600;700&display=swap">
<style>
  :root {
    --backdrop: #e4e4e6;
    --card: #ffffff;
    --band-top: #e9e9f6;
    --band-mid: #6f74c4;
    --band-deep: #1b35a0;
    --rule: #5a5a66;
    --ink: #1a1a1a;
    --mark: #1f4fc8;
  }
  * { margin: 0; padding: 0; box-sizing: border-box; }
  html, body {
    width: 957px;
    height: 1200px;
    overflow: hidden;
    background: var(--backdrop);
    font-family: "Source Sans 3", "Myriad Pro", sans-serif;
    color: var(--ink);
  }
  .sheet { position: relative; width: 957px; height: 1200px; }
  .card {
    position: absolute;
    left: 92px;
    width: 795px;
    height: 454px;
    background: var(--card);
    border-radius: 26px;
    overflow: hidden;
  }
  .card--front { top: 77px; }
  .card--back { top: 639px; }
  .card__band {
    position: absolute;
    left: 0; top: 0;
    width: 94px; height: 100%;
    background: linear-gradient(180deg, var(--band-top) 0%, var(--band-mid) 22%, var(--band-deep) 48%, var(--band-deep) 100%);
  }
  .card__rule {
    position: absolute;
    left: 101px; top: 0;
    width: 4px; height: 100%;
    background: var(--rule);
  }
  .brand__dot {
    position: absolute;
    left: 136px; top: 56px;
    width: 150px; height: 150px;
    border-radius: 50%;
    background: var(--mark);
  }
  .brand__name {
    position: absolute;
    left: 311px; top: 62px;
    font-size: 92px;
    font-weight: 600;
    line-height: 1;
    letter-spacing: 1px;
    color: var(--ink);
  }
  .contact { position: absolute; left: 311px; top: 218px; }
  .contact__name { font-size: 25px; font-weight: 700; line-height: 1; }
  .contact__role { font-size: 19px; font-weight: 700; }
  .contact__line { font-size: 18px; line-height: 1; margin-top: 19px; }
  .contact__line:first-of-type { margin-top: 20px; }
  .contact__line b { font-weight: 700; }
  .contact__sep { margin: 0 6px; }
  .card__address {
    position: absolute;
    left: 162px; top: 403px;
    font-size: 18px;
    line-height: 1;
  }
  .card--back .card__address { left: 158px; top: 403px; }
</style>
</head>
<body>
<main class="sheet">
  <section class="card card--front" aria-label="Business card front">
    <div class="card__band"></div>
    <div class="card__rule"></div>
    <div class="brand__dot" aria-hidden="true"></div>
    <div class="brand__name">Lotvian</div>
    <div class="contact">
      <p class="contact__name">Your Name - <span class="contact__role">Designation</span></p>
      <p class="contact__line"><b>p</b> : 123-456-7890<span class="contact__sep">|</span><b>c</b> : 123-456-7890</p>
      <p class="contact__line"><b>e</b> : name@lotvian.com</p>
      <p class="contact__line"><b>w</b> : www.lotvian.com</p>
    </div>
    <p class="card__address">City Name, Street Name, State Name, Country Code</p>
  </section>

  <section class="card card--back" aria-label="Business card back">
    <div class="card__band"></div>
    <div class="card__rule"></div>
    <div class="brand__dot" aria-hidden="true"></div>
    <div class="brand__name">Lotvian</div>
    <p class="card__address">City Name, Street Name, State Name, Country Code</p>
  </section>
</main>
</body>
</html>
```